Website for Sports and Exercise Medicine Doctor with active research in stem cells therapies.

I am a sports and exercise medicine doctor with research interests in the cutting edge areas of biological therapies, most notable stem cells. None of my patients are dying of anything, and most of them come to see me to decrease their pain, so they can get back to what they want to do.

The approach i then take is to decrease their pain and support them to achieve the things they wish to achieve. Most people start at "Just make it stop hurting doc" , but I try to move them towards something more important over time.

I would like the website to be very different to other "Doctor or medical websites" in its look. No pictures of doctors in white coats and no pictures of fit old people smiling. I would potentially like the fist thing seen to be a quote:

"Less pain. Everybody wants it, but what are you going to do, once you've got it?"

(But this is only an idea, I am open to anything)

The website will need a couple of things

1. "Locations" I work
2. "Research" I am involved in
3. "Sort Me out" - Clinical information for people to access
4. "Social" - imbedded twitter and facebook
5. "Blog" - imbedded wordpress blog
6. "Bio" - the usual bio-stuff

The "Sort Me out" - pages I would like to have the functionality as seen in this site http://www.veltarion.com.au/platelet/. I intend to put disease topics into these pages (eg Achilles tehdinopathy, osteoarthritis etc etc etc). Once again I am not wedded to this but something along these lines would be good.

To give you an idea these are some sites I like
http://www.morbanquilt.com/
http://daptrine.com/
http://ovimbera.com.sg/
http://jolvaniketchup.com/
http://www.pilnorwave.com/
http://quadrisel.com/#offering
http://fennikstudio.tv/
http://norvalgate.com/
http://sablethorn.co.uk/#about

Target Market(s)

20-80 year old.
People with tendon injuries
People with osteoarthritis
People interested in stem cells
I will build the site over time to contain information on multiple sporting injuries and musculoskeletal disorders. It will also become a site for the latest on stem cell research particularly in the area of osteoarthritis.

Industry/Entity Type

Medical

Font styles to use
Sans Serif

Colors
ffffff

Requirements
Nice to have
• To give you an idea these are some sites I like
http://daptrine.com/
http://fennikstudio.tv/
http://norvalgate.com/
Should not have
• Pictures of doctors in white coats or old fit people smiling

```html
<!DOCTYPE html>
<html lang="en">
<head>
<meta charset="utf-8">
<title>dr sk — Sports &amp; Exercise Medicine</title>
<link href="https://fonts.googleapis.com/css2?family=Roboto+Condensed:wght@400;700&family=Roboto:wght@300;400&display=swap" rel="stylesheet">
<style>
  :root {
    --teal: #36768a;
    --ink: #2e2e2e;
    --body: #555555;
    --line: #4a4a4a;
    --social: #cfcfcf;
    --paper: #ffffff;
  }
  * { margin: 0; padding: 0; box-sizing: border-box; }
  html, body { width: 731px; height: 1200px; overflow: hidden; background: var(--paper); }
  .page { position: relative; width: 731px; height: 1200px; font-family: "Roboto", sans-serif; }

  .menu-toggle { position: absolute; left: 97px; top: 16px; width: 15px; height: 11px; }
  .menu-toggle span { display: block; height: 1.5px; background: #9a9a9a; margin-bottom: 3px; }

  .brand {
    position: absolute; top: 62px; left: 0; width: 731px; text-align: center;
    font-family: "Roboto Condensed", sans-serif; font-weight: 400;
    font-size: 84px; line-height: 110px; color: var(--teal); letter-spacing: 2px;
  }

  .tagline {
    position: absolute; top: 195px; left: 0; width: 731px; text-align: center;
    font-family: "Roboto Condensed", sans-serif; font-weight: 700;
    font-size: 27px; line-height: 31px; color: var(--ink);
  }

  .nav-tree { position: absolute; left: 0; top: 292px; }

  .nav-item {
    position: absolute; top: 368px; width: 74px; height: 74px; border-radius: 50%;
    border: 1px solid var(--line); display: flex; align-items: center; justify-content: center;
    font-family: "Roboto", sans-serif; font-size: 9px; color: #444; text-decoration: none;
    text-transform: uppercase;
  }
  .nav-item.is-active { border: 2px solid var(--teal); color: var(--teal); font-weight: 700; }

  .section-band {
    position: absolute; top: 510px; left: 0; width: 731px; height: 70px; background: var(--teal);
    display: flex; align-items: center; justify-content: center;
  }
  .section-band h2 {
    font-family: "Roboto Condensed", sans-serif; font-weight: 700; font-size: 27px;
    color: var(--paper); letter-spacing: 0.3px;
  }
  .band-edge { position: absolute; top: 578px; left: 0; }

  .portrait {
    position: absolute; left: 291px; top: 665px; width: 150px; height: 150px; border-radius: 50%;
    border: 1px solid #777; padding: 3px;
  }
  .portrait div {
    width: 100%; height: 100%; border-radius: 50%;
    background: radial-gradient(circle at 45% 55%, #c9a79a 0%, #b23a3a 35%, #7e1f26 65%, #5b6b52 100%);
  }

  .profile-name {
    position: absolute; top: 823px; left: 0; width: 731px; text-align: center;
    font-family: "Roboto Condensed", sans-serif; font-weight: 700; font-size: 27px; color: var(--ink);
  }
  .profile-role {
    position: absolute; top: 857px; left: 0; width: 731px; text-align: center;
    font-family: "Roboto Condensed", sans-serif; font-weight: 700; font-size: 18px; color: var(--ink);
  }

  .profile-bio {
    position: absolute; top: 900px; left: 92px; width: 547px; text-align: center;
    font-weight: 300; font-size: 12.3px; line-height: 17.7px; color: var(--body);
  }
  .profile-bio p { margin-bottom: 17.7px; }

  .social-links { position: absolute; top: 1108px; left: 0; width: 731px; display: flex; justify-content: center; gap: 2px; }
  .social-links a { width: 26px; height: 26px; border-radius: 50%; background: var(--social); display: block; }
</style>
</head>
<body>
<main class="page">
  <div class="menu-toggle" aria-label="Menu"><span></span><span></span><span></span></div>

  <div class="brand">dr sk</div>

  <h1 class="tagline">Less pain. Everybody wants it, but what are<br>you going to do, once you've got it?</h1>

  <svg class="nav-tree" width="731" height="70" viewBox="0 0 731 70" fill="none" stroke="#4a4a4a" stroke-width="1">
    <line x1="366" y1="0" x2="366" y2="43"/>
    <line x1="138" y1="43" x2="594" y2="43"/>
    <g>
      <path d="M138 43 V64 M133 56 L138 61 L143 56 M133 60 L138 65 L143 60"/>
      <path d="M229 43 V64 M224 56 L229 61 L234 56 M224 60 L229 65 L234 60"/>
      <path d="M320 43 V64 M315 56 L320 61 L325 56 M315 60 L320 65 L325 60"/>
      <path d="M411 43 V64 M406 56 L411 61 L416 56 M406 60 L411 65 L416 60"/>
      <path d="M503 43 V64 M498 56 L503 61 L508 56 M498 60 L503 65 L508 60"/>
      <path d="M594 43 V64 M589 56 L594 61 L599 56 M589 60 L594 65 L599 60"/>
    </g>
  </svg>

  <nav>
    <a class="nav-item is-active" href="#bio" style="left:101px">Bio</a>
    <a class="nav-item" href="#research" style="left:192px">Research</a>
    <a class="nav-item" href="#sort-out" style="left:283px">Sort Out</a>
    <a class="nav-item" href="#clinics" style="left:374px">Clinics</a>
    <a class="nav-item" href="#blog" style="left:466px">Blog</a>
    <a class="nav-item" href="#contact" style="left:557px">Contact</a>
  </nav>

  <section class="section-band"><h2>MEET DR SAM KERROW</h2></section>
  <svg class="band-edge" width="731" height="20" viewBox="0 0 731 20">
    <polygon points="350,2 366,14 382,2" fill="#36768a"/>
    <polyline points="0,5 352,5 366,17 380,5 731,5" fill="none" stroke="#36768a" stroke-width="2"/>
  </svg>

  <div class="portrait"><div role="img" aria-label="Photo of the doctor treating an athlete on the field"></div></div>

  <h3 class="profile-name">Dr Sam Kerrow BSc. B.Med.</h3>
  <p class="profile-role">(Sports Medicine Registrar)</p>

  <div class="profile-bio">
    <p>Dr Kerrow completed a science degree with an honours thesis in Exercise induced Asthma at the University of Harlowe in 1995. He then studied medicine at the University of Brennick completing his degree in 2001. Dr Kerrow served as a registrar for a number of years before pursuing his passion for sport, specialising in Sports Medicine. He has a special interest in groin pain management, overuse injuries in young athletes, boxing medicine and the use of cell therapies for management of tendinopathy and osteoarthritis.</p>
    <p>Dr Kerrow has been involved in a number of elite sporting organisations including the Corvale Herons, Ashmere United and the Northgate Ridge U/18 Teams.</p>
    <p>Dr Kerrow is also currently the team doctor at Tarrow Football Club.</p>
  </div>

  <div class="social-links">
    <a href="#social-1" aria-label="Social link"></a>
    <a href="#social-2" aria-label="Social link"></a>
    <a href="#social-3" aria-label="Social link"></a>
  </div>
</main>
</body>
</html>
```